TALMORK

The business want a professional looking business card. We have a scetch we will add but want the extra upgrade, and would like more suggestions for variations of our business cards.

```html
<!DOCTYPE html>
<html lang="en">
<head>
<meta charset="utf-8">
<title>TALMORK – Business Card</title>
<link rel="stylesheet" href="https://fonts.googleapis.com/css2?family=Playfair+Display:wght@500;600&family=Montserrat:wght@400;600&family=Open+Sans:wght@400&display=swap">
<style>
  :root {
    --backdrop: #cccccc;
    --ink: #000000;
    --paper: #ffffff;
    --gold-light: #f2d480;
    --gold-mid: #c9a55a;
    --gold-dark: #7d5f2a;
    --gold-pale: #e3d3a0;
    --text-grey: #5e5e5e;
    --gold-sweep: linear-gradient(90deg, var(--gold-pale) 0%, var(--gold-mid) 30%, var(--gold-light) 52%, var(--gold-mid) 72%, var(--gold-dark) 100%);
  }
  * { margin: 0; padding: 0; box-sizing: border-box; }
  html, body {
    width: 1200px; height: 1200px; overflow: hidden;
    background: var(--backdrop);
  }
  .canvas { position: relative; width: 1200px; height: 1200px; }

  /* Front card */
  .card-front {
    position: absolute; left: 347px; top: 251px;
    width: 519px; height: 297px;
    background: var(--gold-sweep);
    padding: 6px;
  }
  .card-front__field {
    position: relative; width: 100%; height: 100%;
    background: var(--ink);
  }
  .brand {
    position: absolute; left: 0; right: 0; top: 38px;
    display: flex; flex-direction: column; align-items: center;
  }
  .brand__mark {
    width: 58px; height: 58px; border-radius: 50%;
    border: 3px solid var(--gold-mid);
    margin-bottom: 26px;
  }
  .brand__name {
    font-family: "Playfair Display", serif; font-weight: 500;
    font-size: 25px; letter-spacing: 14px; padding-left: 14px;
    color: var(--gold-mid); line-height: 1;
  }
  .brand__since {
    margin-top: 8px;
    font-family: "Montserrat", sans-serif; font-weight: 400;
    font-size: 10px; letter-spacing: 3.5px; padding-left: 3.5px;
    color: var(--gold-mid);
  }
  .name-band {
    position: absolute; left: 0; right: 0; top: 221px; height: 40px;
    background: var(--gold-sweep);
    display: flex; align-items: center; justify-content: center; gap: 12px;
  }
  .name-band__text {
    font-family: "Playfair Display", serif; font-weight: 600;
    font-size: 27px; color: var(--ink); line-height: 1;
    transform: scaleX(0.82); letter-spacing: -0.5px;
  }
  .name-band__dot { width: 8px; height: 8px; border-radius: 50%; background: var(--ink); }

  /* Back card */
  .card-back {
    position: absolute; left: 343px; top: 587px;
    width: 520px; height: 296px;
    background: var(--paper);
    overflow: hidden;
  }
  .card-back__decor {
    position: absolute; left: 0; top: 0; width: 176px; height: 100%;
    background: linear-gradient(135deg, var(--gold-mid) 0%, var(--gold-light) 45%, var(--gold-dark) 100%);
    opacity: 0.85;
  }
  .holder { position: absolute; left: 183px; top: 34px; }
  .holder__name {
    font-family: "Montserrat", sans-serif; font-weight: 600;
    font-size: 27px; line-height: 1;
    background: linear-gradient(90deg, var(--gold-dark), var(--gold-mid) 40%, var(--gold-mid) 60%, var(--gold-dark));
    -webkit-background-clip: text; background-clip: text; color: transparent;
  }
  .holder__role {
    margin-top: 10px;
    font-family: "Montserrat", sans-serif; font-weight: 400;
    font-size: 19px; color: var(--text-grey);
  }
  .divider {
    position: absolute; left: 185px; top: 147px; width: 312px; height: 2px;
    background: var(--gold-sweep);
  }
  .contacts { position: absolute; left: 182px; top: 170px; list-style: none; }
  .contacts__item {
    display: flex; align-items: center; gap: 11px; height: 30px;
    font-family: "Open Sans", sans-serif; font-size: 20px; color: var(--text-grey);
  }
  .contacts__icon { width: 26px; height: 26px; flex: none; }
</style>
</head>
<body>
<div class="canvas">
  <svg width="0" height="0" style="position:absolute">
    <defs>
      <linearGradient id="gold-ring" x1="0" y1="0" x2="1" y2="1">
        <stop offset="0" stop-color="#c9a55a"/>
        <stop offset=".5" stop-color="#f2d480"/>
        <stop offset="1" stop-color="#7d5f2a"/>
      </linearGradient>
    </defs>
  </svg>

  <section class="card-front" aria-label="Business card front">
    <div class="card-front__field">
      <div class="brand">
        <span class="brand__mark" aria-hidden="true"></span>
        <span class="brand__name">TALMORK</span>
        <span class="brand__since">SINCE 2026</span>
      </div>
    </div>
    <div class="name-band">
      <span class="name-band__dot"></span>
      <span class="name-band__text">TALMORK SOLVANG</span>
      <span class="name-band__dot"></span>
    </div>
  </section>

  <section class="card-back" aria-label="Business card back">
    <div class="card-back__decor" role="img" aria-label="Gold ornamental emblem decoration"></div>
    <div class="holder">
      <h1 class="holder__name">Lars Henrik Solvang</h1>
      <p class="holder__role">CEO &amp; Founder</p>
    </div>
    <div class="divider"></div>
    <ul class="contacts">
      <li class="contacts__item">
        <svg class="contacts__icon" viewBox="0 0 26 26" aria-hidden="true">
          <circle cx="13" cy="13" r="11.5" fill="none" stroke="url(#gold-ring)" stroke-width="2"/>
          <path d="M9 8.5c.6-.6 1.3-.6 1.7 0l1 1.4c.3.5.2 1-.2 1.4l-.6.5c.6 1.3 1.6 2.3 2.9 2.9l.5-.6c.4-.4.9-.5 1.4-.2l1.4 1c.6.4.6 1.1 0 1.7l-.8.8c-3.4.3-7.9-4.2-7.6-7.6z" fill="#b8934a"/>
        </svg>
        <span>004795418276</span>
      </li>
      <li class="contacts__item">
        <svg class="contacts__icon" viewBox="0 0 26 26" aria-hidden="true">
          <circle cx="13" cy="13" r="11.5" fill="none" stroke="url(#gold-ring)" stroke-width="2"/>
          <rect x="7.5" y="9" width="11" height="8" rx="1" fill="#d8b96a"/>
          <path d="M7.8 9.4l5.2 4 5.2-4" fill="none" stroke="#ffffff" stroke-width="1"/>
        </svg>
        <span>hello@talmork.llc</span>
      </li>
      <li class="contacts__item">
        <svg class="contacts__icon" viewBox="0 0 26 26" aria-hidden="true">
          <circle cx="13" cy="13" r="11.5" fill="none" stroke="url(#gold-ring)" stroke-width="2"/>
          <g fill="none" stroke="#b8934a" stroke-width="1">
            <circle cx="13" cy="13" r="5.5"/>
            <ellipse cx="13" cy="13" rx="2.3" ry="5.5"/>
            <path d="M7.5 13h11M8.3 10.3h9.4M8.3 15.7h9.4"/>
          </g>
        </svg>
        <span>www.talmork.llc</span>
      </li>
    </ul>
  </section>
</div>
</body>
</html>
```